Business Card Design

I'd like to have some business cards designed using my new logo. I am an accountant and company secretary and offer these services through Holloway Meridian Advisory Pty Ltd. I am the sole Director of the company. Please let me know if you require any further logo files.

Industry/Entity Type

Business

```html
<!DOCTYPE html>
<html lang="en">
<head>
<meta charset="utf-8">
<title>Holloway Meridian Advisory – Business Card</title>
<link href="https://fonts.googleapis.com/css2?family=Cinzel:wght@400&family=Montserrat:wght@500&family=Arimo:wght@400&display=swap" rel="stylesheet">
<style>
  :root {
    --backdrop: #e9e9e7;
    --card-white: #ffffff;
    --brand-blue: #1f7fd0;
    --card-blue-light: #2f95dd;
    --card-blue-deep: #1d7cca;
    --ink-black: #0d0d0d;
    --logo-grey: #6b6b6b;
    --rule-grey: #9a9a9a;
    --stripe-dark: #22313d;
    --paper-text: #ffffff;
  }
  * { box-sizing: border-box; margin: 0; padding: 0; }
  html, body { width: 1200px; height: 900px; overflow: hidden; }
  body {
    background: var(--backdrop);
    position: relative;
  }
  .card {
    position: absolute;
    left: 320px;
    width: 560px;
    height: 320px;
    border-radius: 4px;
    overflow: hidden;
    box-shadow: 0 10px 26px rgba(0,0,0,0.18);
  }

  /* Front */
  .card--front { top: 100px; background: var(--card-white); }
  .accent-bar {
    position: absolute;
    top: 196px;
    height: 18px;
    background: var(--brand-blue);
    border-radius: 9px;
  }
  .accent-bar--left { left: -12px; width: 222px; }
  .accent-bar--right { right: -12px; width: 200px; }
  .brand-lockup {
    position: absolute;
    top: 118px;
    left: 222px;
    display: flex;
    align-items: flex-end;
    gap: 12px;
  }
  .brand-dot {
    width: 34px; height: 34px;
    border-radius: 50%;
    background: var(--brand-blue);
    margin-bottom: 2px;
  }
  .brand-divider {
    width: 1.5px;
    height: 66px;
    background: var(--rule-grey);
  }
  .brand-name {
    font-family: "Cinzel", "Times New Roman", serif;
    font-weight: 400;
    font-size: 17px;
    line-height: 21px;
    letter-spacing: 1.2px;
    color: var(--logo-grey);
    text-transform: uppercase;
    white-space: nowrap;
  }

  /* Back */
  .card--back {
    top: 480px;
    background: radial-gradient(ellipse at 60% 30%, var(--card-blue-light), var(--card-blue-deep) 75%);
  }
  .corner-stripes { position: absolute; top: 0; right: 40px; }
  .name-tab {
    position: absolute;
    top: 118px;
    left: 0;
    width: 250px;
    height: 66px;
    background: var(--ink-black);
    border-radius: 0 33px 33px 0;
    padding: 10px 0 0 26px;
    color: var(--paper-text);
  }
  .name-tab__name {
    font-family: "Montserrat", Arial, sans-serif;
    font-weight: 500;
    font-size: 22px;
    letter-spacing: 2px;
    font-variant: small-caps;
    line-height: 26px;
  }
  .name-tab__role {
    font-family: "Arimo", Arial, sans-serif;
    font-size: 15px;
    line-height: 20px;
  }
  .contact-icon { position: absolute; }
  .contact-icon--pin { top: 212px; left: 30px; }
  .contact-icon--phone { top: 250px; left: 30px; }
  .contact-icon--web { top: 290px; left: 30px; }
  .contact-icon--mail { top: 214px; left: 224px; }
</style>
</head>
<body>
  <section class="card card--front" aria-label="Card front">
    <span class="accent-bar accent-bar--left"></span>
    <span class="accent-bar accent-bar--right"></span>
    <div class="brand-lockup">
      <span class="brand-dot"></span>
      <span class="brand-divider"></span>
      <p class="brand-name">Holloway<br>Meridian<br>Advisory Pty Ltd</p>
    </div>
  </section>

  <section class="card card--back" aria-label="Card back">
    <svg class="corner-stripes" width="60" height="90" viewBox="0 0 60 90" aria-hidden="true">
      <line x1="6" y1="0" x2="36" y2="90" stroke="var(--stripe-dark)" stroke-width="3"/>
      <line x1="20" y1="0" x2="50" y2="90" stroke="var(--stripe-dark)" stroke-width="3"/>
    </svg>
    <div class="name-tab">
      <p class="name-tab__name">Your Name</p>
      <p class="name-tab__role">Designation</p>
    </div>
    <svg class="contact-icon contact-icon--pin" width="18" height="24" viewBox="0 0 18 24" aria-label="Address">
      <path d="M9 1a7.5 7.5 0 0 0-7.5 7.5C1.5 14 9 23 9 23s7.5-9 7.5-14.5A7.5 7.5 0 0 0 9 1z" fill="#fff"/>
      <circle cx="9" cy="8.5" r="2.8" fill="var(--card-blue-deep)"/>
    </svg>
    <svg class="contact-icon contact-icon--phone" width="18" height="28" viewBox="0 0 18 28" aria-label="Phone">
      <rect x="2" y="1" width="14" height="26" rx="3" fill="none" stroke="#fff" stroke-width="1.8"/>
      <line x1="2" y1="5" x2="16" y2="5" stroke="#fff" stroke-width="1.2"/>
      <line x1="2" y1="22" x2="16" y2="22" stroke="#fff" stroke-width="1.2"/>
    </svg>
    <svg class="contact-icon contact-icon--web" width="20" height="20" viewBox="0 0 20 20" aria-label="Website">
      <g fill="none" stroke="#fff" stroke-width="1.4">
        <circle cx="10" cy="10" r="8.5"/>
        <ellipse cx="10" cy="10" rx="3.8" ry="8.5"/>
        <line x1="1.5" y1="10" x2="18.5" y2="10"/>
        <path d="M3 5.5h14M3 14.5h14"/>
      </g>
    </svg>
    <svg class="contact-icon contact-icon--mail" width="26" height="18" viewBox="0 0 26 18" aria-label="Email">
      <rect x="0" y="0" width="26" height="18" rx="1.5" fill="#fff"/>
      <path d="M1 1l12 9 12-9M1 17l9-8M25 17l-9-8" fill="none" stroke="var(--card-blue-deep)" stroke-width="1.4"/>
    </svg>
  </section>
</body>
</html>
```